Company raising consciousness thru leadership & self-awareness needs amazing Letterhead

We are a technology company that spun out of a consulting firm. We are waking people up in corporate America through surveys, leadership development, workshops and consulting. Getting employees to become self-aware and changing company culture through improved leadership and team effectiveness. We need Word letterhead for our proposals, handouts, and worksheets that match our brand standard, is fresh, and communicates trust, credibility and professionalism.

Target Market(s)

Our target clients are other businesses, and executive leaders and C-suite leaders in those companies.

Font styles to use
Sans Serif

Requirements
Must have
• A Word template we can use for handouts, proposals, executive summary, project management documents, and letters. We need our logo. Please add page number and date on the footer. Must match the theme of our new website in look and feel to match the brand we are trying to promote. Use the colors from our brand standard document I submitted.

```html
<!DOCTYPE html>
<html lang="en">
<head>
<meta charset="utf-8">
<title>Verantis Letterhead – Front Page &amp; Inner Page</title>
<link href="https://fonts.googleapis.com/css2?family=Montserrat:wght@400;500;600;700&family=Poppins:wght@500;600&display=swap" rel="stylesheet">
<style>
  :root {
    --brand-purple: #7b4397;
    --brand-navy: #2b3a6b;
    --brand-sky: #3aa3d8;
    --wash-light: #e4edf4;
    --wash-mid: #d3e2ee;
    --text-grey: #555a66;
    --paper: #ffffff;
    --canvas: #ffffff;
  }
  * { box-sizing: border-box; margin: 0; padding: 0; }
  html, body {
    width: 1200px; height: 1200px; overflow: hidden;
    background: var(--canvas);
    font-family: "Montserrat", sans-serif;
  }
  .stage { position: relative; width: 1200px; height: 1200px; }

  .presentation-title {
    position: absolute; left: 72px; top: 44px;
    font-family: "Poppins", sans-serif; font-weight: 600;
    font-size: 34px; color: var(--brand-purple); letter-spacing: 0.2px;
  }
  .presentation-subtitle {
    position: absolute; left: 74px; top: 98px;
    font-family: "Poppins", sans-serif; font-weight: 500;
    font-size: 19px; color: var(--brand-navy);
  }

  .sheet {
    position: absolute; background: var(--paper); overflow: hidden;
    box-shadow: 0 0 6px 2px rgba(120, 110, 115, 0.45);
  }
  .sheet--front { left: 398px; top: 38px; width: 752px; height: 976px; }
  .sheet--inner { left: 54px; top: 234px; width: 719px; height: 934px; }

  .header-wash {
    position: absolute; left: 0; top: 0;
    background: radial-gradient(ellipse at 35% 45%, var(--wash-mid) 0%, var(--wash-light) 55%, rgba(228,237,244,0) 100%);
  }
  .sheet--front .header-wash { width: 330px; height: 160px; }
  .sheet--inner .header-wash { width: 280px; height: 72px; }

  .brand { position: absolute; display: flex; align-items: center; }
  .brand-mark { flex: none; border-radius: 50%; border-style: solid; border-color: var(--brand-purple); }
  .brand-name { font-weight: 600; color: var(--brand-navy); letter-spacing: 1px; line-height: 1; }

  .sheet--front .brand { left: 14px; top: 30px; gap: 14px; }
  .sheet--front .brand-mark { width: 86px; height: 86px; border-width: 3px; }
  .sheet--front .brand-name { font-size: 38px; }

  .sheet--inner .brand { left: 14px; top: 18px; gap: 8px; }
  .sheet--inner .brand-mark { width: 40px; height: 40px; border-width: 2px; }
  .sheet--inner .brand-name { font-size: 20px; letter-spacing: 0.5px; }

  .contact-block {
    position: absolute; right: 32px; top: 38px; text-align: right;
    font-size: 13px; line-height: 19.5px; color: var(--text-grey);
  }
  .contact-block .contact-strong { color: var(--brand-purple); font-weight: 600; }

  .contact-line {
    position: absolute; right: 30px; top: 30px;
    font-size: 10px; font-weight: 700; color: var(--brand-purple);
  }

  .footer-band {
    position: absolute; left: 0;
    background: linear-gradient(90deg, var(--brand-purple) 0%, var(--brand-purple) 78%, rgba(123,67,151,0) 100%);
  }
  .sheet--front .footer-band { top: 941px; width: 500px; height: 35px; }
  .sheet--inner .footer-band { top: 900px; width: 478px; height: 34px; }

  .page-meta {
    position: absolute; color: var(--brand-purple); font-weight: 600;
  }
  .page-meta .page-label { font-weight: 500; }
  .sheet--front .page-meta { right: 32px; top: 949px; font-size: 12px; }
  .sheet--inner .page-meta { right: 30px; top: 909px; font-size: 11.5px; }
</style>
</head>
<body>
<main class="stage">
  <h1 class="presentation-title">Revised Design</h1>
  <p class="presentation-subtitle">Front Page &amp; Inner Page</p>

  <section class="sheet sheet--front" aria-label="Letterhead front page">
    <div class="header-wash" role="img" aria-label="Soft light-blue watercolour wash behind the brand name"></div>
    <div class="brand">
      <span class="brand-mark"></span>
      <span class="brand-name">VERANTIS</span>
    </div>
    <address class="contact-block" style="font-style: normal;">
      4172 Harlow Avenue, Suite #204<br>
      Westbrook, FL 32904<br>
      <span class="contact-strong">555-0147-2368</span><br>
      <span class="contact-strong">vrngroup.com</span>
    </address>
    <div class="footer-band" role="img" aria-label="Purple brush-stroke band along the page foot"></div>
    <p class="page-meta">20-12-2020, <span class="page-label">Page</span> &nbsp;|&nbsp; 1</p>
  </section>

  <section class="sheet sheet--inner" aria-label="Letterhead inner page">
    <div class="header-wash" role="img" aria-label="Soft light-blue watercolour wash behind the brand name"></div>
    <div class="brand">
      <span class="brand-mark"></span>
      <span class="brand-name">VERANTIS</span>
    </div>
    <p class="contact-line">555-0147-2368, vrngroup.com</p>
    <div class="footer-band" role="img" aria-label="Purple brush-stroke band along the page foot"></div>
    <p class="page-meta">20-12-2020, <span class="page-label">Page</span> &nbsp;|&nbsp; 2</p>
  </section>
</main>
</body>
</html>
```